Web-Design for Electrcian Company

Our Customer is a small business electrian in Switzerland. He is looking for a fresh and innovative website design. He is well known for his extra service, and that they always go for the extra-mile! In his logo you also see that positive and fresh image the try to bring to the customer. the main colors are black, red and white.

the website structure will be:

- home
- services (with submenu for each service)
- references (with submenu for each category of services)
- about us (2 submenus: history and staff)
- links
- Contact

Reason: We are discussing the Proposals with the customer right now

Target Market(s)

Architects, building owners, people from the age of 35 up...

Industry/Entity Type

Small Business

```html
<!DOCTYPE html>
<html lang="de">
<head>
<meta charset="utf-8">
<title>Brunner + Team Elektro AG</title>
<link rel="stylesheet" href="https://fonts.googleapis.com/css2?family=Ubuntu:wght@400;500;700&family=PT+Serif:wght@400;700&family=Bebas+Neue&family=Oswald:wght@400;500&family=Arimo:ital,wght@0,400;1,400&display=swap">
<style>
:root{
  --red:#d81f2a;
  --red-dark:#b5141f;
  --red-nav-top:#e2313c;
  --ink:#1b1b1b;
  --grey-text:#8a8a8a;
  --heading-grey:#4a4a4a;
  --page-grey:#ececec;
  --white:#ffffff;
  --frame:#dcdcdc;
}
*{margin:0;padding:0;box-sizing:border-box}
html,body{width:968px;height:1200px;overflow:hidden;background:var(--white)}
body{position:relative;font-family:"Arimo",Arial,sans-serif;color:var(--ink)}
.abs{position:absolute}

.header{left:0;top:0;width:968px;height:94px;background:linear-gradient(#e9e9e9,#fbfbfb 40%,#f1f1f1)}
.brand{left:114px;top:32px;font-family:"Ubuntu",sans-serif;font-weight:500;font-size:22px;color:var(--ink);letter-spacing:-.2px}
.brand-mark{left:395px;top:9px;width:76px;height:76px;border:4px solid var(--red);border-radius:50%}
.contact-lines{right:114px;top:50px;text-align:right;font-family:"Ubuntu",sans-serif;font-size:13.5px;line-height:19px;color:var(--red)}

.nav{left:0;top:94px;width:968px;height:37px;background:linear-gradient(var(--red-nav-top),var(--red-dark));border-bottom:1px solid #8e0e16}
.nav ul{list-style:none;position:absolute;left:114px;top:0;display:flex}
.nav li{width:122px;height:37px;line-height:37px;text-align:center;font-family:"PT Serif",serif;font-weight:700;font-size:11px;color:var(--white);text-transform:uppercase;border-left:1px solid #8e0e16}
.nav li:first-child{border-left:none;width:126px;background:linear-gradient(#c01a24,#e02f3a)}

.stage{left:0;top:131px;width:968px;height:306px;background:var(--page-grey)}
.slider{left:113px;top:161px;width:740px;height:247px;background:var(--frame);border-radius:12px}
.slider-inner{left:9px;top:9px;width:722px;height:230px;background:var(--white);border-radius:8px;overflow:hidden}
.portrait{left:0;top:6px;width:205px;height:224px;background:linear-gradient(160deg,#c9a386,#8b5f4a 60%,#2a1e1e)}
.slide-title{left:279px;top:16px;font-family:"Ubuntu",sans-serif;font-weight:500;font-size:25px;color:var(--red)}
.slide-sub{left:279px;top:46px;font-family:"PT Serif",serif;font-size:23px;color:#555;letter-spacing:.4px}
.slide-text{left:280px;top:78px;width:413px;font-size:9.3px;line-height:16.6px;color:#555}
.btn{left:280px;top:155px;width:121px;height:30px;background:linear-gradient(#e8333d,#c4161f);border-radius:3px;color:var(--white);font-family:"Oswald",sans-serif;font-weight:500;font-size:14px;line-height:30px;padding-left:13px;letter-spacing:.3px}
.btn svg{position:absolute;right:14px;top:10px}
.slide-rule{left:280px;top:198px;width:413px;height:2px;background:#eeeeee}
.dots{left:667px;top:211px;display:flex;gap:4px}
.dots span{width:6px;height:6px;border-radius:50%;background:#c8c8c8}
.dots span.on{background:#3aa1d8}

.section-title{left:114px;top:456px;font-family:"Bebas Neue",sans-serif;font-size:33px;color:var(--red);letter-spacing:.3px}
.tile{width:236px;height:152px;border:1px solid #c5c5c5}
.caption{font-family:"Ubuntu",sans-serif;font-weight:500;font-size:13.5px;color:#3c3c3c}

.divider{left:114px;top:910px;width:740px;height:3px;background:#e3e3e3}
.col-title{top:936px;font-family:"Bebas Neue",sans-serif;font-size:26px;color:var(--heading-grey)}
.date{font-family:"Oswald",sans-serif;font-size:13px;color:var(--red);letter-spacing:-.3px}
.news-text{width:222px;font-size:8.8px;line-height:16px;color:var(--grey-text);text-align:justify}
.quote{left:367px;top:973px;width:221px;font-style:italic;font-size:8.8px;line-height:16px;color:var(--grey-text);text-align:justify}
.quote-name{left:367px;top:1092px;font-style:italic;font-weight:700;font-size:8.8px;color:#555}
.quote-link{left:367px;top:1106px;font-style:italic;font-size:8.8px;color:var(--red);text-decoration:underline}
.member{width:71px;height:62px;border:2px solid var(--white);box-shadow:0 1px 3px rgba(0,0,0,.35);background:linear-gradient(160deg,#b89474,#6e5140)}

.footer{left:0;top:1151px;width:968px;height:49px;background:linear-gradient(var(--red-nav-top),var(--red-dark))}
.footer-text{left:114px;top:15px;font-family:"Ubuntu",sans-serif;font-weight:400;font-size:13.5px;color:var(--white)}
.social{top:16px;width:18px;height:18px;border-radius:3px;background:#5a8fc3;border:1px solid #ffffff}
</style>
</head>
<body>

<header class="header abs">
  <div class="brand abs">Brunner + Team Elektro AG</div>
  <div class="brand-mark abs"></div>
  <div class="contact-lines abs">Tel - 071/555 20 40<br>Fax - 071/555 20 41</div>
</header>

<nav class="nav abs">
  <ul>
    <li>Home</li><li>Services</li><li>Refrences</li><li>About Us</li><li>Links</li><li>Contacts</li>
  </ul>
</nav>

<section class="stage abs"></section>
<div class="slider abs">
  <div class="slider-inner abs">
    <div class="portrait abs" role="img" aria-label="Portrait photo of a team member"></div>
    <div class="slide-title abs">Brunner + Team Elektro AG</div>
    <div class="slide-sub abs">Complete Electrical Solutions</div>
    <p class="slide-text abs">Lorem Ipsum is simply dummy text of the printing and typesetting industry. Lorem Ipsum has been the industry's standard dummy text ever since the 1500s, when an unknown printer took a galley of type and scrambled it to make a type specimen book. It has survived not only five centuries, but also the leap into electronic typesetting, remaining essentially unchanged.</p>
    <div class="btn abs">CONTACT ME
      <svg width="6" height="10" viewBox="0 0 6 10"><path d="M0 0L6 5L0 10Z" fill="#fff"/></svg>
    </div>
    <div class="slide-rule abs"></div>
    <div class="dots abs"><span></span><span class="on"></span><span></span></div>
  </div>
</div>

<h1 class="section-title abs">Solutions for all your electrical requirements:</h1>

<div class="tile abs" style="left:114px;top:510px;background:linear-gradient(#f6f6f6,#e2e2e2)" role="img" aria-label="Recessed ceiling light"></div>
<div class="caption abs" style="left:115px;top:673px">Licht (house / office / outdoor)</div>
<div class="tile abs" style="left:368px;top:510px;background:linear-gradient(120deg,#8a8f56,#b9b89a 55%,#6f7548)" role="img" aria-label="Outdoor wall lamp by a balcony"></div>
<div class="caption abs" style="left:369px;top:673px">Aussenbeleuchtung</div>
<div class="tile abs" style="left:620px;top:510px;background:linear-gradient(120deg,#9ba3ad,#3d4550 60%,#6c737c)" role="img" aria-label="Network cabinet with cabling"></div>
<div class="caption abs" style="left:621px;top:673px">EDV / ADSL</div>

<div class="tile abs" style="left:114px;top:709px;background:linear-gradient(100deg,#8b5a2f 0 8%,#d9bba6 8%,#c9a893)" role="img" aria-label="Switchboard with circuit breakers"></div>
<div class="caption abs" style="left:115px;top:872px">Steuerung</div>
<div class="tile abs" style="left:368px;top:709px;background:linear-gradient(90deg,#d5d5d8,#f4f4f6 40%,#c9c9cc)" role="img" aria-label="Telephone system unit"></div>
<div class="caption abs" style="left:369px;top:872px">Telefonanlage</div>
<div class="tile abs" style="left:620px;top:709px;background:linear-gradient(#e6e6e6,#d2d2d2)" role="img" aria-label="Door bell panel"></div>
<div class="caption abs" style="left:621px;top:872px">Sonnerie</div>

<div class="divider abs"></div>

<h2 class="col-title abs" style="left:114px">News/RSS</h2>
<div class="date abs" style="left:114px;top:973px">Jan.13.2012</div>
<p class="news-text abs" style="left:114px;top:995px">Lorem Ipsum is simply dummy text of the printing and typesetting industry. Lorem Ipsum has been the industry's standard dummy text ever since the 1500s.</p>
<div class="date abs" style="left:114px;top:1052px">Feb.18.2012</div>
<p class="news-text abs" style="left:114px;top:1074px">Lorem Ipsum is simply dummy text of the printing and typesetting industry. Lorem Ipsum has been the industry's standard dummy text ever since the 1500s.</p>

<h2 class="col-title abs" style="left:366px">Testimonials</h2>
<p class="quote abs">Lorem Ipsum is simply dummy text of the printing and typesetting industry. Lorem Ipsum has been the industry's standard dummy text ever since the 1500s, when an unknown printer took a galley of type and scrambled it to make a type specimen book. It has survived not only five centuries, but also the leap into electronic typesetting, remaining.</p>
<div class="quote-name abs">Mr. Lorem Ipsim</div>
<div class="quote-link abs">View All Testimonials</div>

<h2 class="col-title abs" style="left:619px">Meet our Team</h2>
<div class="member abs" style="left:619px;top:972px" role="img" aria-label="Team member photo"></div>
<div class="member abs" style="left:701px;top:972px" role="img" aria-label="Team member photo"></div>
<div class="member abs" style="left:783px;top:972px;background:linear-gradient(160deg,#7d8a4a,#c9a07c)" role="img" aria-label="Team member photo"></div>
<div class="member abs" style="left:619px;top:1053px" role="img" aria-label="Team member photo"></div>
<div class="member abs" style="left:701px;top:1053px;background:#3f3f3f" role="img" aria-label="Team member photo">
  <svg class="abs" style="left:28px;top:24px" width="12" height="12" viewBox="0 0 12 12"><path d="M6 0V12M0 6H12" stroke="#fff" stroke-width="2.4"/></svg>
</div>
<div class="member abs" style="left:783px;top:1053px;background:linear-gradient(160deg,#e8e8e8,#b58a6e)" role="img" aria-label="Team member photo"></div>

<footer class="footer abs">
  <div class="footer-text abs">Brunner + Team Elektro AG &nbsp;© 2012. All Rights Reserved &nbsp;| &nbsp;Privacy Policy</div>
  <div class="social abs" style="left:792px" aria-label="Professional network"></div>
  <div class="social abs" style="left:829px" aria-label="Social network"></div>
</footer>

</body>
</html>
```